Crestvale Mining Webpage

Need a website for a copper mining company that is seeking financing and /or partners with small mines. We need a website that will give basic information regarding the property we are seeking financing for, and background information of the owners (about us), current opportunity page that will convey our value added proposition, along with a 'contact us' page.

Please review other mining companies website for ideas
Any clarity needed we will communicate with you, please ask if you are uncertain.

We will likely provide more information as the design develops

Target Market(s)

Investment companies and Mining professionals

Industry/Entity Type

Mining

Number of Pages Required

4 page

Font styles to use
Sans Serif

Colors

Designer to choose colors to be used in the design.

Requirements
Must have
• I am looking to have a template which I can use later as well to add my own content. Please be sure to have each item (designs, links buttons, drop down menus)its own file so I can import into the web formats
• Also please provide primary colors used as RGB values.
• Include a list of fonts used.
• Pages see attached power point slides
• 1) About us - what we do (2 slide of the .ppt attached) need to leave room for a mission and vision statement
• 2) current opportunities (see word document and Slide 5 as results)
• 3) Value Add ideas ( pages 3)
• 4) Management (our photos Slide 4 of the deck) with room to type background information
• 5) Events and current information (this will be a page listing dates of events, and also blog entries.)
• Let us know if you can't open a .ppt file
Nice to have
• Non-cartoonish look, it should be a polished website
• Drop down menu format
• Scrolling format with an image in the background
• Contact information page (see first slide of slide deck)
• Feel free to use the photos as needed through out the site

```html
<!DOCTYPE html>
<html lang="en">
<head>
<meta charset="utf-8">
<title>Crestvale Mining</title>
<link href="https://fonts.googleapis.com/css2?family=Cinzel:wght@400;700&family=Lato:wght@400;700&display=swap" rel="stylesheet">
<style>
:root{
  --green:#1fa84f;
  --green-dark:#178a40;
  --ink:#222;
  --text:#444;
  --muted:#777;
  --red:#c8102e;
  --dark:#1e1e1e;
  --rock:#4a3526;
  --white:#fff;
}
*{box-sizing:border-box;margin:0;padding:0}
html,body{width:1200px;height:3913px;overflow:hidden}
body{font-family:'Lato',sans-serif;color:var(--text);background:var(--white);position:relative}
.abs{position:absolute}

.topbar{left:0;top:0;width:1200px;height:26px;background:var(--green);color:#fff;font-size:12px}
.topbar .contact{position:absolute;right:50px;top:6px;display:flex;gap:22px;align-items:center}
.topbar svg{vertical-align:-2px;margin-right:5px}

.header{left:0;top:26px;width:1200px;height:104px;background:#fff}
.brand{position:absolute;left:118px;top:36px;font-family:'Cinzel',serif;font-size:25px;letter-spacing:2px;color:var(--ink)}
.nav{position:absolute;left:440px;top:34px;display:flex;align-items:center;font-size:13px;font-weight:700;color:var(--ink)}
.nav span{padding:0 18px;border-left:1px solid #ccc;line-height:14px}
.nav span:first-child{border-left:none;color:var(--green);text-decoration:underline}

.hero{left:0;top:130px;width:1200px;height:556px;background:linear-gradient(180deg,#3d3c3a 0%,#6b6255 40%,#8a7a62 60%,#3a3632 100%)}
.hero-title{position:absolute;left:0;width:1200px;top:626px;text-align:center;font-family:'Cinzel',serif;font-weight:700;font-size:34px;color:#fff;letter-spacing:1px}
.hero-arrow{position:absolute;top:640px}

.section-title{position:absolute;left:0;width:1200px;text-align:center;font-family:'Cinzel',serif;font-size:30px;color:var(--ink);letter-spacing:1px}
.section-title .g{color:var(--green)}
.rule{position:absolute;left:440px;width:320px;height:1px;background:#bbb}
.rule::after{content:"";position:absolute;left:152px;top:-7px;width:14px;height:14px;background:#fff;border:2px solid var(--ink);transform:rotate(45deg)}
.rule.light{background:rgba(255,255,255,.6)}
.rule.light::after{background:var(--rock);border-color:#fff}

.readmore{position:absolute;left:0;width:1200px;top:1054px;text-align:center;font-size:14px;font-weight:700;color:var(--green);text-decoration:underline}

.solutions{left:0;top:1170px;width:1200px;height:521px;background:radial-gradient(ellipse at 50% 50%,#6b4d35 0%,#4a3526 55%,#2c1f16 100%)}
.sol-item{position:absolute;top:1420px;width:170px;text-align:center;color:#fff;font-size:15px;font-weight:700;line-height:20px}
.sol-item .circle{width:102px;height:102px;border-radius:50%;background:#fff;border:4px solid #ddd;margin:0 auto 42px;display:flex;align-items:center;justify-content:center}

.card{position:absolute;top:1890px;width:264px;height:410px}
.card.active{border:2px solid var(--green)}
.card .photo{width:262px;height:166px;background:linear-gradient(160deg,#bdbab5,#7c7872)}
.card h3{font-size:21px;color:var(--red);margin:20px 0 2px 0;font-weight:700}
.card .role{font-size:15px;color:var(--ink);font-weight:700}
.card ul{margin-top:16px;padding-top:10px;border-top:1px solid #ddd;list-style:none;font-size:11px;line-height:15px;color:#555}
.card li{padding-left:12px;position:relative;margin-bottom:10px}
.card li::before{content:"";position:absolute;left:2px;top:6px;width:4px;height:4px;border-radius:50%;background:#555}

.cta{left:0;top:2422px;width:1200px;height:253px;background:linear-gradient(90deg,#0c0c0c 0%,#1b1b1b 55%,#3a3a3a 70%,#111 100%)}
.cta h2{position:absolute;left:122px;top:80px;font-size:26px;color:#fff;font-weight:700}
.cta .btn{position:absolute;left:165px;top:138px;width:143px;height:42px;background:var(--green);color:#fff;font-size:14px;font-weight:700;line-height:42px;padding-left:18px}

.fin-box{position:absolute;top:2879px;width:286px;height:180px;border:1px solid #ccc;box-shadow:0 2px 4px rgba(0,0,0,.15);background:#fff}
.fin{position:absolute;top:3074px;width:290px}
.fin h3{font-size:19px;color:var(--green);font-weight:700;line-height:24px;min-height:48px}
.fin ul{list-style:none;font-size:11px;line-height:17px;color:#555;margin-top:4px}
.fin li{padding-left:12px;position:relative}
.fin li::before{content:"";position:absolute;left:2px;top:7px;width:4px;height:4px;border-radius:50%;background:#555}

.inquiry{left:0;top:3236px;width:1200px;height:314px;background:var(--green);color:#fff}
.inquiry h2{position:absolute;left:124px;top:110px;font-family:'Cinzel',serif;font-size:34px;font-weight:400;line-height:38px}
.inquiry p{position:absolute;left:124px;top:200px;width:250px;font-size:11px;line-height:18px}
.inquiry .lead{position:absolute;left:474px;top:104px;font-size:17px;font-weight:700}
.field{position:absolute;width:284px;height:38px;background:#fff;color:#888;font-size:11px;padding:12px 10px}
.inquiry .send{position:absolute;left:474px;top:246px;width:136px;height:38px;background:#111;color:#fff;font-size:13px;font-weight:700;line-height:38px;padding-left:18px}

.footer{left:0;top:3550px;width:1200px;height:363px;background:linear-gradient(180deg,#3a3a3a,#262626)}
.f-info{position:absolute;top:66px;width:360px;text-align:center;color:#ddd;font-size:12px}
.f-info svg{display:block;margin:0 auto 10px}
.f-brand{position:absolute;left:0;width:1200px;top:170px;text-align:center;font-family:'Cinzel',serif;font-size:24px;letter-spacing:2px;color:#fff}
.f-nav{position:absolute;left:0;width:1200px;top:264px;display:flex;justify-content:center;font-size:12px;font-weight:700;color:#fff}
.f-nav span{padding:0 20px;border-left:1px solid #888}
.f-nav span:first-child{border-left:none}
.f-bottom{position:absolute;left:0;top:314px;width:1200px;height:49px;border-top:1px solid #555}
.f-bottom .copy{position:absolute;left:118px;top:16px;font-size:11px;color:#ccc}
.f-bottom .social{position:absolute;right:120px;top:10px;display:flex;gap:8px}
.f-bottom .social span{width:28px;height:28px;border-radius:50%;background:#3b6fb6}
</style>
</head>
<body>

<div class="abs topbar">
  <div class="contact">
    <span><svg width="12" height="12" viewBox="0 0 24 24"><path fill="#fff" d="M6.6 10.8a15.1 15.1 0 006.6 6.6l2.2-2.2c.3-.3.7-.4 1-.2 1.1.4 2.3.6 3.6.6.6 0 1 .4 1 1V20c0 .6-.4 1-1 1A17 17 0 013 4c0-.6.4-1 1-1h3.5c.6 0 1 .4 1 1 0 1.3.2 2.5.6 3.6.1.3 0 .7-.2 1z"/></svg>012-555-0147</span>
    <span><svg width="13" height="10" viewBox="0 0 26 20"><rect x="1" y="1" width="24" height="18" rx="2" fill="none" stroke="#fff" stroke-width="2"/><path d="M1 2l12 9 12-9" fill="none" stroke="#fff" stroke-width="2"/></svg>dhartwell@crestvalemining.net</span>
  </div>
</div>

<header class="abs header">
  <div class="brand">Crestvale Mining</div>
  <nav class="nav">
    <span>HOME</span><span>ABOUT ▾</span><span>OPPORTUNITIES</span><span>OUR TEAM</span><span>EVENTS</span><span>CONTACT US</span>
  </nav>
</header>

<div class="abs hero" role="img" aria-label="Interior of a copper ore processing mill with large grinding drums and steel walkways"></div>
<div class="hero-title">THE GREAT MINING EXPERIENCE COMPANY</div>
<svg class="hero-arrow" style="left:90px" width="14" height="26" viewBox="0 0 14 26"><path d="M12 2L2 13l10 11" fill="none" stroke="#fff" stroke-width="2"/></svg>
<svg class="hero-arrow" style="left:1096px" width="14" height="26" viewBox="0 0 14 26"><path d="M2 2l10 11L2 24" fill="none" stroke="#fff" stroke-width="2"/></svg>

<h2 class="section-title" style="top:764px">ABOUT CRESTVALE MINING</h2>
<div class="rule" style="top:822px"></div>

<svg class="abs" style="left:120px;top:880px" width="900" height="160" viewBox="0 0 900 160" font-family="Lato,sans-serif">
  <rect x="4" y="40" width="372" height="48" fill="#fff" stroke="#1fa84f" stroke-width="2"/>
  <text x="14" y="58" font-size="12" font-weight="700" fill="#1fa84f">Form a new copper focused Mining Company</text>
  <circle cx="18" cy="76" r="2" fill="#444"/>
  <text x="26" y="80" font-size="12" fill="#444">Acquire majority in small scale producing operations</text>
  <rect x="590" y="20" width="272" height="92" fill="#fff" stroke="#1fa84f" stroke-width="2"/>
  <text x="600" y="40" font-size="12" font-weight="700" fill="#1fa84f">Targets are:</text>
  <circle cx="604" cy="56" r="2" fill="#444"/><text x="612" y="60" font-size="12" fill="#444">Under-capitalized</text>
  <circle cx="604" cy="74" r="2" fill="#444"/><text x="612" y="78" font-size="12" fill="#444">Hold numerous under-explored concessions</text>
  <circle cx="604" cy="92" r="2" fill="#444"/><text x="612" y="96" font-size="12" fill="#444">Located in proven mining districts</text>
  <polygon points="366,12 494,12 430,110" fill="#fff" stroke="#1fa84f" stroke-width="2"/>
  <text text-anchor="middle" font-size="12" font-weight="700" fill="#1fa84f"><tspan x="430" y="28">Immediate</tspan><tspan x="430" y="42">Operating</tspan><tspan x="430" y="56">Cash</tspan><tspan x="430" y="70">Flow</tspan></text>
  <polygon points="498,30 436,136 560,136" fill="#fff" stroke="#1fa84f" stroke-width="2"/>
  <text text-anchor="middle" font-size="12" font-weight="700" fill="#1fa84f"><tspan x="498" y="72">High</tspan><tspan x="498" y="86">Probability</tspan><tspan x="498" y="100">for added</tspan><tspan x="498" y="114">Value and</tspan><tspan x="498" y="128">Growth</tspan></text>
</svg>
<div class="readmore">READ MORE &gt;&gt;</div>

<div class="abs solutions" role="img" aria-label="Close-up texture of raw copper ore rock"></div>
<h2 class="section-title" style="top:1252px;color:#fff">OUR SOLUTIONS</h2>
<div class="rule light" style="top:1310px"></div>
<div class="abs" style="left:200px;top:1471px;width:800px;border-top:2px dashed rgba(255,255,255,.5)"></div>

<div class="sol-item" style="left:130px"><div class="circle">
  <svg width="56" height="56" viewBox="0 0 56 56"><path d="M8 14h40L28 46z" fill="none" stroke="#777" stroke-width="3"/><circle cx="28" cy="24" r="5" fill="#777"/></svg>
  </div>Ownership<br>Consolidation</div>
<div class="sol-item" style="left:322px"><div class="circle">
  <svg width="56" height="56" viewBox="0 0 56 56"><circle cx="28" cy="22" r="12" fill="none" stroke="#777" stroke-width="3"/><path d="M12 50c2-10 8-14 16-14s14 4 16 14" fill="none" stroke="#777" stroke-width="3"/></svg>
  </div>Management With<br>Track Record In District</div>
<div class="sol-item" style="left:515px"><div class="circle">
  <svg width="56" height="56" viewBox="0 0 56 56"><text x="28" y="42" text-anchor="middle" font-family="Lato,sans-serif" font-size="40" fill="#777">$</text></svg>
  </div>Smart Low<br>Level Capital</div>
<div class="sol-item" style="left:707px"><div class="circle">
  <svg width="56" height="56" viewBox="0 0 56 56"><rect x="8" y="30" width="28" height="12" fill="#777"/><path d="M36 34l12-14v20" fill="none" stroke="#777" stroke-width="3"/><circle cx="14" cy="46" r="4" fill="#777"/><circle cx="30" cy="46" r="4" fill="#777"/></svg>
  </div>Exploration<br>Drilling</div>
<div class="sol-item" style="left:900px"><div class="circle">
  <svg width="56" height="56" viewBox="0 0 56 56"><rect x="10" y="36" width="7" height="10" fill="#777"/><rect x="21" y="28" width="7" height="18" fill="#777"/><rect x="32" y="20" width="7" height="26" fill="#777"/><path d="M8 30L40 10" stroke="#777" stroke-width="3"/></svg>
  </div>Increased Profits &amp;<br>Company Value</div>

<h2 class="section-title" style="top:1774px"><span class="g">OUR</span> TEAM</h2>
<div class="rule" style="top:1832px"></div>

<div class="card" style="left:138px">
  <div class="photo" role="img" aria-label="Portrait photo of the CEO"></div>
  <h3>Daniel Hartwell</h3><div class="role">CEO</div>
  <ul>
    <li>13 yr mining experience</li>
    <li>Masters in Mining Engineering from Westfield School of Mines.</li>
    <li>Former General Manager Northgate Metals Ridgeview</li>
    <li>Proven history of UG mine production growth and reserve increases</li>
    <li>Passed all roles at Open Pit and Underground Operations: Superintendent up to General Manager</li>
  </ul>
</div>
<div class="card active" style="left:466px;height:408px">
  <div class="photo" style="width:260px" role="img" aria-label="Portrait photo of the COO"></div>
  <div style="padding:0 8px">
  <h3>Rodrigo Valdés</h3><div class="role">COO</div>
  <ul>
    <li>9 yr mining experience</li>
    <li>Current General Manager of Santa Rosa &amp; Alameda</li>
    <li>Currently 3% owner of Las Piedras</li>
    <li>Born and raised in the district well connected</li>
  </ul></div>
</div>
<div class="card" style="left:796px">
  <div class="photo" role="img" aria-label="Portrait photo of the legal counsel"></div>
  <h3>Lucía Benavente</h3><div class="role">Legal Consul</div>
  <ul>
    <li>15 yr mining experience</li>
    <li>Local Counsel for Alto Norte Project (Cerro Blanco-Caspana)</li>
    <li>Local Counsel for Ridgeline Quebrada Mine</li>
    <li>Currently 6% owner of Las Piedras</li>
  </ul>
</div>

<div class="abs cta" role="img" aria-label="Miners with headlamps in a dark underground tunnel"></div>
<div class="abs cta" style="background:none">
  <h2>THE SMALL INDEPENDENT MINING COMPANY</h2>
  <div class="btn">CONTACT US &gt;</div>
</div>

<h2 class="section-title" style="top:2753px"><span class="g">FINANCIALS AND</span> GROWTH CASES</h2>
<div class="rule" style="top:2812px"></div>

<svg width="0" height="0" style="position:absolute">
  <defs>
    <g id="npv-chart" font-family="Lato,sans-serif">
      <text x="143" y="20" text-anchor="middle" font-size="11" font-weight="700" fill="#222">NPV 8%</text>
      <text x="14" y="100" font-size="8" fill="#444" transform="rotate(-90 14 100)" text-anchor="middle">Million USD</text>
      <g font-size="8" fill="#444" text-anchor="end">
        <text x="36" y="38">14</text><text x="36" y="62">10</text><text x="36" y="86">6</text><text x="36" y="110">2</text><text x="36" y="134">0</text>
      </g>
      <line x1="40" y1="34" x2="40" y2="134" stroke="#aaa"/>
      <line x1="40" y1="134" x2="270" y2="134" stroke="#aaa"/>
      <rect x="62" y="128" width="14" height="6" fill="#e8432a"/><rect x="80" y="122" width="14" height="12" fill="#f7a823"/>
      <rect x="140" y="124" width="14" height="10" fill="#e8432a"/><rect x="158" y="106" width="14" height="28" fill="#f7a823"/>
      <rect x="218" y="116" width="14" height="18" fill="#e8432a"/><rect x="236" y="64" width="14" height="70" fill="#f7a823"/>
      <g font-size="8" fill="#444" text-anchor="middle">
        <text x="78" y="146">Base Case</text><text x="156" y="146">Case 1</text><text x="234" y="146">Case 2</text>
      </g>
      <rect x="118" y="154" width="6" height="6" fill="#e8432a"/><text x="127" y="160" font-size="8" fill="#444">5yr</text>
      <rect x="148" y="154" width="6" height="6" fill="#f7a823"/><text x="157" y="160" font-size="8" fill="#444">8yr</text>
    </g>
  </defs>
</svg>

<div class="fin-box" style="left:144px"><svg width="286" height="180"><use href="#npv-chart"/></svg></div>
<div class="fin-box" style="left:462px"><svg width="286" height="180"><use href="#npv-chart"/></svg></div>
<div class="fin-box" style="left:782px"><svg width="286" height="180"><use href="#npv-chart"/></svg></div>

<div class="fin" style="left:146px"><h3>Base Case Op Improvements</h3>
  <ul><li>Operational Improvements</li><li>Open increase, hire mine and plant managers</li><li>Increase head grade &amp; mill rec.</li><li>Capex = $4M (purchase price)</li></ul></div>
<div class="fin" style="left:464px"><h3>Case 1: Mill + Exploration</h3>
  <ul><li>Base Case operational improvements</li><li>Plant (12.5 tn/month to 17 tn/m)</li><li>Exploration drilling (10,000m)</li><li>Capex = $6.4M (incl. purchase)</li></ul></div>
<div class="fin" style="left:784px"><h3>Mill + Exploration + Mine Development</h3>
  <ul><li>Base Case operational improvements</li><li>Plant (12.5 tn/month to 17 tn/m)</li><li>Exploration drilling (10,000m)</li><li>Capex = $6.4M (incl. purchase)</li></ul></div>

<section class="abs inquiry">
  <h2>QUICK<br>INQUIRY</h2>
  <p>Send us a short note about your project or investment interest and our team will reply within two working days [+]</p>
  <div class="lead">Please fill up bellow form</div>
  <div class="field" style="left:474px;top:146px">Name</div>
  <div class="field" style="left:766px;top:146px">Email</div>
  <div class="field" style="left:474px;top:194px">Phone</div>
  <div class="field" style="left:766px;top:194px">Message</div>
  <div class="send">READ MORE ▸</div>
</section>

<footer class="abs footer">
  <div role="img" aria-label="Faint city street map behind the footer" style="position:absolute;inset:0;background:linear-gradient(135deg,rgba(255,255,255,.03),rgba(255,255,255,.06))"></div>
  <div class="f-info" style="left:80px">
    <svg width="16" height="22" viewBox="0 0 16 22"><path d="M8 1a7 7 0 00-7 7c0 5 7 13 7 13s7-8 7-13a7 7 0 00-7-7z" fill="none" stroke="#ccc" stroke-width="1.5"/><circle cx="8" cy="8" r="2.5" fill="#ccc"/></svg>
    123, Lorem Ipsum Street Name, City Name 01245</div>
  <div class="f-info" style="left:420px">
    <svg width="20" height="20" viewBox="0 0 24 24"><path fill="none" stroke="#ccc" stroke-width="1.5" d="M6.6 10.8a15.1 15.1 0 006.6 6.6l2.2-2.2c.3-.3.7-.4 1-.2 1.1.4 2.3.6 3.6.6.6 0 1 .4 1 1V20c0 .6-.4 1-1 1A17 17 0 013 4c0-.6.4-1 1-1h3.5c.6 0 1 .4 1 1 0 1.3.2 2.5.6 3.6.1.3 0 .7-.2 1z"/></svg>
    <b style="color:#fff">Phone: 012-555-0147</b></div>
  <div class="f-info" style="left:760px">
    <svg width="20" height="20" viewBox="0 0 20 20"><path d="M1 9L19 1l-6 18-3-8z" fill="none" stroke="#ccc" stroke-width="1.5"/></svg>
    Email: dhartwell@crestvalemining.net</div>
  <div class="f-brand">Crestvale Mining</div>
  <div class="f-nav"><span>HOME</span><span>ABOUT</span><span>OPPORTUNITIES</span><span>OUR TEAM</span><span>EVENTS</span><span>CONTACT US</span></div>
  <div class="f-bottom">
    <div class="copy">Copyright © 2019 Crestvale Mining. All Right Reserved</div>
    <div class="social"><span></span><span></span><span></span><span style="background:#d24a3a"></span></div>
  </div>
</footer>

</body>
</html>
```